Bright Ridge Electric Needs A Logo Design

We need a logo for my new company based out of Sacramento, Ca called Bright Ridge Electric. The name says it all, my electrical contracting business provides "Bright Ridge Professional Work" I'm open to any colors that pop and customers to say Wow. I would love to print my cards on metal.

Industry/Entity Type

Business

Contact Information for Business Card

The card needs to have as follows
Name of company: Bright Ridge Electric
My Name: Dorian Pelko
Phone # 916-382-5507
CL# 2087396
Email: brightridgeelectric@mailvance.net
and a slogan that represent "BRIGHT RIDGE"

Requirements
Must have
• The card needs to have as follows
• Name of company: Bright Ridge Electric
• My Name : Dorian Pelko
• Phone # 916-382-5507
• CL# 2087396
• Email: brightridgeelectric@mailvance.net
• and a slogan that represent "BRIGHT RIDGE"
Nice to have
• popping colors
• electrical Arcing

```html
<!DOCTYPE html>
<html lang="en">
<head>
<meta charset="utf-8">
<title>Bright Ridge Electric – Business Card</title>
<link rel="stylesheet" href="https://fonts.googleapis.com/css2?family=Gelasio:wght@400&family=Arimo:wght@400&display=swap">
<style>
  :root {
    --page-bg: #ffffff;
    --card-deep: #140b45;
    --card-mid: #2b3590;
    --card-glow: #1aa6e0;
    --card-glow-core: #2bb3e6;
    --wordmark: #ffffff;
    --name-gold: #f6c21c;
    --badge-gold: #f7c70d;
    --contact-text: #ffffff;
  }
  html, body {
    margin: 0;
    padding: 0;
    width: 1200px;
    height: 999px;
    overflow: hidden;
    background: var(--page-bg);
  }
  .canvas {
    position: relative;
    width: 1200px;
    height: 999px;
  }
  .business-card {
    position: absolute;
    left: 72px;
    top: 204px;
    width: 1050px;
    height: 599px;
    overflow: hidden;
    background:
      radial-gradient(ellipse 520px 430px at 568px 100px,
        var(--card-glow-core) 0%,
        var(--card-glow) 22%,
        #1d6fbf 40%,
        var(--card-mid) 62%,
        #1f1f6a 80%,
        var(--card-deep) 100%);
  }
  .brand-badge {
    position: absolute;
    left: 310px;
    top: 104px;
    width: 136px;
    height: 136px;
    border-radius: 50%;
    background: var(--badge-gold);
  }
  .wordmark {
    position: absolute;
    left: 471px;
    top: 104px;
    margin: 0;
    font-family: "Gelasio", Georgia, serif;
    font-weight: 400;
    color: var(--wordmark);
    line-height: 1;
  }
  .wordmark-primary {
    display: block;
    font-size: 70px;
  }
  .wordmark-secondary {
    display: block;
    margin-top: 6px;
    font-size: 45px;
  }
  .holder-name {
    position: absolute;
    left: 66px;
    top: 366px;
    margin: 0;
    font-family: "Gelasio", Georgia, serif;
    font-weight: 400;
    font-size: 43px;
    color: var(--name-gold);
    line-height: 1;
  }
  .contact-list {
    position: absolute;
    left: 67px;
    top: 447px;
    margin: 0;
    padding: 0;
    list-style: none;
    font-family: "Arimo", Helvetica, Arial, sans-serif;
    font-size: 26px;
    line-height: 35px;
    color: var(--contact-text);
  }
</style>
</head>
<body>
  <main class="canvas">
    <section class="business-card" aria-label="Bright Ridge Electric business card">
      <div class="brand-badge" aria-hidden="true"></div>
      <h1 class="wordmark">
        <span class="wordmark-primary">Bright Ridge</span>
        <span class="wordmark-secondary">ELECTRIC</span>
      </h1>
      <h2 class="holder-name">Dorian Pelko</h2>
      <ul class="contact-list">
        <li class="contact-phone">Phone # 916-382-5507</li>
        <li class="contact-license">CL# 2087396</li>
        <li class="contact-email">Email: brightridgeelectric@mailvance.net</li>
      </ul>
    </section>
  </main>
</body>
</html>
```